Kelvora Ledger Web Design Contest

We would like for you to design a website for www.kelvoraledger-example.com. Kelvora Ledger is a CPA Firm offering accounting, auditing, and tax preparation services.

We would like to have a consistent feel with the logo, business card, envelope, and stationary designs that were created by another designer on PlanHive. Examples of each are attached. We would like the website to have a clean/modern style.

The website should include the following:

1. A general "Welcome" landing page
2. A "About the Company" page
3. A "Services Offered" page
4. A "Contact Us" form
5. A button for "Sign up for Newsletter"

Target Market(s)

Individuals and businesses that require accounting, auditing, and tax preparation services from a CPA.

Industry/Entity Type

Accounting

Coding

Number of Pages Required

5+ page

Font styles to use
Other font styles liked:
• Trebuchet or similar

Requirements
Must have
• Consistent feel with logo and letterhead. The gray and blue bar on the letterhead should be incorporated into the website design.

```html
<!DOCTYPE html>
<html lang="en">
<head>
<meta charset="utf-8">
<title>Kelvora Ledger</title>
<link href="https://fonts.googleapis.com/css2?family=Montserrat:wght@400;500;700&family=Open+Sans:wght@300;400;600&display=swap" rel="stylesheet">
<style>
:root{
  --navy:#0a2266;
  --blue:#0d2c8c;
  --ink:#222;
  --muted:#666;
  --band:#ececec;
  --white:#fff;
  --grey:#555;
}
*{margin:0;padding:0;box-sizing:border-box}
html,body{width:796px;height:1200px;overflow:hidden;background:var(--white)}
body{position:relative;font-family:"Open Sans",sans-serif;color:var(--ink)}
.abs{position:absolute}
.topline{left:0;top:0;width:796px;height:3px;background:var(--navy)}
.notch{left:408px;top:3px;width:0;height:0;border-left:7px solid transparent;border-right:7px solid transparent;border-top:7px solid var(--navy)}
.brand{left:55px;top:10px;width:150px;text-align:center}
.brand-square{width:36px;height:36px;border:2px solid var(--navy);margin:0 auto 4px}
.brand-name{font-family:"Montserrat",sans-serif;font-weight:500;font-size:10.5px;color:var(--navy);white-space:nowrap}
.brand-tag{font-family:"Montserrat",sans-serif;font-size:6.5px;color:var(--ink);letter-spacing:.3px}
.nav{top:37px;font-family:"Montserrat",sans-serif;font-size:11.5px;font-weight:500;color:var(--ink)}
.nav.active{color:var(--navy)}
.hero{left:0;top:83px;width:796px;height:345px;background:linear-gradient(100deg,#d9d3cf 0%,#cfc6bf 35%,#e6e3df 60%,#c9b4a8 100%)}
.arrow{top:228px;width:31px;height:31px;border:1px solid #333;background:rgba(255,255,255,.25);display:flex;align-items:center;justify-content:center}
.hero-mark{left:535px;top:152px;width:68px;height:68px;border:3px solid #333}
.hero-title{left:400px;width:350px;top:236px;text-align:center;font-family:"Montserrat",sans-serif;font-weight:700;font-size:36px;color:var(--navy)}
.hero-sub{left:420px;width:310px;top:290px;text-align:center;font-family:"Montserrat",sans-serif;font-size:13.5px;line-height:17px;color:#111}
.dot{top:402px;width:9px;height:9px;border:1px solid #333}
.dot.on{background:#111}
.welcome{left:0;top:428px;width:796px;height:312px;background:var(--band)}
.h2{left:0;width:796px;text-align:center;font-weight:300;font-size:28px;color:var(--blue)}
.intro{left:125px;width:546px;top:513px;text-align:center;font-size:11.5px;line-height:19.5px;color:#333}
.btn{left:342px;top:587px;width:112px;height:36px;background:var(--blue);border:2px solid var(--navy);border-radius:3px;color:var(--white);font-family:"Montserrat",sans-serif;font-size:10px;font-weight:500;display:flex;align-items:center;justify-content:center}
.card{top:711px;width:221px;height:173px;background:var(--navy);color:var(--white);text-align:center}
.card-shade{top:882px;width:221px;height:12px}
.circle{top:658px;width:108px;height:108px;border-radius:50%;background:var(--white);border:4px solid var(--navy);display:flex;align-items:center;justify-content:center}
.circle div{width:74px;height:64px;border-radius:40%}
.card h3{margin-top:70px;font-family:"Montserrat",sans-serif;font-weight:700;font-size:13.5px}
.card p{margin-top:6px;font-size:9.5px;line-height:14px}
.card a{display:inline-block;margin-top:6px;font-weight:600;font-size:11px;color:var(--white);text-decoration:underline}
.news-p{left:168px;width:460px;top:972px;text-align:center;font-size:10px;line-height:17px;color:var(--muted)}
.email{left:208px;top:1027px;width:380px;height:41px;border:1px solid #999;display:flex;align-items:center;justify-content:space-between;padding:0 14px;font-size:13px;color:#555}
.contact{left:0;top:1096px;width:796px;height:69px;background:var(--band)}
.cicon{top:1115px;width:35px;height:35px;border:1px solid var(--navy);display:flex;align-items:center;justify-content:center}
.ctext{top:1116px;font-size:10px;line-height:15.5px;color:#111}
.footer{left:0;top:1165px;width:796px;height:35px;background:var(--navy)}
.copy{left:53px;top:1176px;font-size:10px;color:#aab}
.copy b{font-weight:400;color:var(--white)}
.social{top:1165px;width:28px;height:35px;background:var(--blue)}
</style>
</head>
<body>
<div class="abs topline"></div>
<div class="abs notch"></div>

<header>
  <div class="abs brand">
    <div class="brand-square"></div>
    <div class="brand-name">KELVORA LEDGER, LLC</div>
    <div class="brand-tag">Accounting · Audit · Tax Services</div>
  </div>
  <nav>
    <span class="abs nav active" style="left:400px">HOME</span>
    <span class="abs nav" style="left:472px">ABOUT US</span>
    <span class="abs nav" style="left:576px">SERVICES</span>
    <span class="abs nav" style="left:670px">CONTACT US</span>
  </nav>
</header>

<section>
  <div class="abs hero" role="img" aria-label="Photo of a businesswoman holding a laptop over a desk with reports and a calculator"></div>
  <div class="abs arrow" style="left:10px"><svg width="12" height="12" viewBox="0 0 12 12"><path d="M6 2 2 6l4 4M10 2 6 6l4 4" fill="none" stroke="#111" stroke-width="1.3"/></svg></div>
  <div class="abs arrow" style="left:756px"><svg width="12" height="12" viewBox="0 0 12 12"><path d="M2 2l4 4-4 4M6 2l4 4-4 4" fill="none" stroke="#111" stroke-width="1.3"/></svg></div>
  <div class="abs hero-mark"></div>
  <div class="abs hero-title">Kelvora Ledger</div>
  <div class="abs hero-sub">is a CPA Firm offering accounting, auditing, and tax preparation services.</div>
  <div class="abs dot" style="left:373px"></div>
  <div class="abs dot on" style="left:394px"></div>
  <div class="abs dot" style="left:414px"></div>
</section>

<section>
  <div class="abs welcome"></div>
  <h2 class="abs h2" style="top:458px">Welcome to Kelvora Ledger</h2>
  <p class="abs intro">Lorem ipsum dolor sit amet, consectetur adipiscing elit, sed do eiusmod tempor incididunt ut labore et dolore magna aliqua. Ut enim ad minim veniam, quis nostrud exercitation ullamco laboris nisi ut aliquip ex ea commodo consequat. Duis aute irure.</p>
  <div class="abs btn">KNOW MORE</div>
</section>

<section>
  <div class="abs card" style="left:51px"><h3>ACCOUNTING</h3><p>Lorem ipsum dolor sit amet,<br>consectetur adipiscing elit</p><a>Read More</a></div>
  <div class="abs card" style="left:287px"><h3>AUDITING</h3><p>Lorem ipsum dolor sit amet,<br>consectetur adipiscing elit</p><a>Read More</a></div>
  <div class="abs card" style="left:523px"><h3>TAX PREPARATION</h3><p>Lorem ipsum dolor sit amet,<br>consectetur adipiscing elit</p><a>Read More</a></div>
  <svg class="abs card-shade" style="left:51px" viewBox="0 0 221 12"><defs><radialGradient id="sh" cx=".5" cy="0" r=".6"><stop offset="0" stop-color="#fff"/><stop offset="1" stop-color="#777"/></radialGradient></defs><path d="M0 2Q110 16 221 2V0H0Z" fill="url(#sh)"/></svg>
  <svg class="abs card-shade" style="left:287px" viewBox="0 0 221 12"><path d="M0 2Q110 16 221 2V0H0Z" fill="url(#sh)"/></svg>
  <svg class="abs card-shade" style="left:523px" viewBox="0 0 221 12"><path d="M0 2Q110 16 221 2V0H0Z" fill="url(#sh)"/></svg>
  <div class="abs circle" style="left:105px"><div role="img" aria-label="Illustration of gold coin stacks and banknotes" style="background:radial-gradient(#f2c43a,#c9c2a8)"></div></div>
  <div class="abs circle" style="left:344px"><div role="img" aria-label="Illustration of a folder under a magnifying glass" style="background:radial-gradient(#e9b86a,#9a8e80)"></div></div>
  <div class="abs circle" style="left:580px"><div role="img" aria-label="Illustration of coins, banknotes and a percent sign" style="background:radial-gradient(#f39a1c,#8fb77a)"></div></div>
</section>

<section>
  <h2 class="abs h2" style="top:921px">Sign up For NewsLetter</h2>
  <p class="abs news-p">Lorem ipsum dolor sit amet, consectetur adipiscing elit, sed do eiusmod tempor incididunt ut labore et dolore magna aliqua</p>
  <div class="abs email"><span>Email Id here</span><svg width="18" height="14" viewBox="0 0 18 14"><rect width="18" height="14" rx="2" fill="#111"/><path d="M1 2l8 6 8-6" fill="none" stroke="#fff" stroke-width="1.4"/></svg></div>
</section>

<footer>
  <div class="abs contact"></div>
  <div class="abs cicon" style="left:51px"><svg width="13" height="12" viewBox="0 0 13 12"><path d="M6.5 0 0 5.5h2V12h3.3V8h2.4v4H11V5.5h2Z" fill="var(--navy)"/></svg></div>
  <div class="abs ctext" style="left:98px">218 Harlow Crest Road, Suite<br>410, Marlow, GA 30999</div>
  <div class="abs cicon" style="left:344px"><svg width="12" height="12" viewBox="0 0 12 12"><path d="M2 0h2.5l1 3-1.5 1.2a7 7 0 0 0 3.8 3.8L9 6.5l3 1V10a2 2 0 0 1-2 2A10 10 0 0 1 0 2a2 2 0 0 1 2-2Z" fill="var(--navy)"/></svg></div>
  <div class="abs ctext" style="left:392px">555 014 2290</div>
  <div class="abs cicon" style="left:566px"><svg width="13" height="10" viewBox="0 0 13 10"><rect width="13" height="10" rx="1.5" fill="var(--navy)"/><path d="M1 1.5l5.5 4 5.5-4" fill="none" stroke="#fff" stroke-width="1.1"/></svg></div>
  <div class="abs ctext" style="left:614px">mara@kelvoraledger-example.com</div>
  <div class="abs footer"></div>
  <div class="abs copy">© <b>KELVORA LEDGER</b> - 2015. All Rights Reserved.</div>
  <div class="abs social" style="left:661px;background:var(--grey)" aria-label="Social link"></div>
  <div class="abs social" style="left:689px" aria-label="Social link"></div>
  <div class="abs social" style="left:717px" aria-label="Social link"></div>
</footer>
</body>
</html>
```